E-Waste Recycling Company Business Card

New Electronic Recycling Company based in Long Island, New York called "Baron Rustwell" We take outdated computers, components, electrical wire, circuit breakers, ink cartridges, etc. We look mostly for donated items that we recycle for our customers but will pay for large quantities from businesses. The design should reflect that we are environmentally friendly and our unique Quadra Purge process that ensures all personal data is wiped clean off hard drives. Please use our attached logo
Electrical

```html
<!DOCTYPE html>
<html lang="en">
<head>
<meta charset="utf-8">
<title>Baron Rustwell – Business Card</title>
<link href="https://fonts.googleapis.com/css2?family=Montserrat:wght@700&family=Questrial&display=swap" rel="stylesheet">
<style>
  :root {
    --canvas: #e9eae7;
    --card-white: #fbfbfb;
    --card-grey: #eeeeee;
    --green: #3fa635;
    --green-light: #6cc24a;
    --green-dark: #1f7a1d;
    --green-deep: #2b8a2a;
    --ink: #3d3d3d;
    --ink-soft: #555555;
  }
  * { box-sizing: border-box; margin: 0; padding: 0; }
  html, body { width: 1200px; height: 900px; overflow: hidden; }
  body {
    background: var(--canvas);
    display: flex;
    align-items: center;
    justify-content: center;
    gap: 48px;
    font-family: "Questrial", sans-serif;
  }
  .card {
    position: relative;
    width: 540px;
    height: 309px;
    overflow: hidden;
    box-shadow: 0 6px 18px rgba(0,0,0,.18);
  }
  /* Front */
  .card-front {
    background: linear-gradient(135deg, var(--card-white) 0%, var(--card-grey) 100%);
  }
  .card-front .wave { position: absolute; inset: 0; width: 100%; height: 100%; }
  .contact {
    position: absolute;
    left: 62px;
    top: 40px;
    color: var(--ink-soft);
  }
  .contact .name {
    font-family: "Montserrat", sans-serif;
    font-weight: 700;
    font-size: 13px;
    letter-spacing: .6px;
    color: var(--ink);
  }
  .contact .role {
    font-size: 11px;
    color: var(--green);
    margin: 4px 0 8px;
  }
  .contact ul { list-style: none; }
  .contact li {
    display: flex;
    align-items: center;
    gap: 8px;
    font-size: 10.5px;
    line-height: 17px;
  }
  .contact li svg { width: 10px; height: 10px; flex: none; }
  .contact li.no-icon { padding-left: 18px; }
  .brand {
    position: absolute;
    display: flex;
    align-items: center;
    gap: 10px;
    font-family: "Questrial", sans-serif;
    font-size: 22px;
    white-space: nowrap;
  }
  .card-front .brand { right: 40px; top: 150px; color: var(--green-dark); }
  .brand .dot {
    width: 34px; height: 34px;
    border-radius: 50%;
  }
  .card-front .brand .dot { background: var(--green); }
  /* Back */
  .card-back {
    background: radial-gradient(ellipse at 50% 35%, var(--green-light) 0%, var(--green) 45%, var(--green-deep) 100%);
  }
  .card-back .brand {
    left: 50%; top: 50%;
    transform: translate(-50%, -50%);
    color: #ffffff;
    font-size: 28px;
  }
  .card-back .brand .dot { background: #ffffff; width: 40px; height: 40px; }
</style>
</head>
<body>

  <section class="card card-front">
    <svg class="wave" viewBox="0 0 540 309" preserveAspectRatio="none" aria-hidden="true">
      <path d="M0,120 C110,200 300,245 540,280 L540,309 L0,309 Z" fill="#d8ecd3"/>
      <path d="M0,138 C120,215 310,258 540,292 L540,309 L0,309 Z" fill="var(--green-light)"/>
      <path d="M0,170 C140,240 320,272 540,300 L540,309 L0,309 Z" fill="var(--green)"/>
      <path d="M0,250 C160,285 340,300 540,306 L540,309 L0,309 Z" fill="var(--green-dark)" opacity=".5"/>
    </svg>

    <div class="contact">
      <p class="name">ELIAS MARROW, GSC</p>
      <p class="role">President</p>
      <ul>
        <li class="no-icon">1180 Harlow Lane Millbrook, BC, V0X 1R2</li>
        <li>
          <svg viewBox="0 0 10 10"><path d="M2,1 L4,1 L4.5,3 L3.3,4 C4,5.5 4.5,6 6,6.7 L7,5.5 L9,6 L9,8 C9,8.6 8.6,9 8,9 C4,9 1,6 1,2 C1,1.4 1.4,1 2,1 Z" fill="var(--green)"/></svg>
          250.555.0142
        </li>
        <li>
          <svg viewBox="0 0 10 10"><rect x="1" y="4" width="8" height="5" rx="1" fill="var(--green)"/><rect x="3" y="1" width="4" height="3" fill="none" stroke="var(--green)" stroke-width="1"/></svg>
          250.555.0187
        </li>
        <li>
          <svg viewBox="0 0 10 10"><rect x="1" y="2" width="8" height="6" fill="none" stroke="var(--green)" stroke-width="1"/><path d="M1,2 L5,5.5 L9,2" fill="none" stroke="var(--green)" stroke-width="1"/></svg>
          elias.marrow@email.com
        </li>
      </ul>
    </div>

    <div class="brand"><span class="dot"></span>Baron Rustwell</div>
  </section>

  <section class="card card-back">
    <div class="brand"><span class="dot"></span>Baron Rustwell</div>
  </section>

</body>
</html>
```